Women's Health Company needs business card

We need a business card for a USA based women's health care company. We use digital technology to enhance therapy prescribed by clinicians for their patients

```html
<!DOCTYPE html>
<html lang="en">
<head>
<meta charset="utf-8">
<title>Velora Health – Business Card</title>
<link rel="stylesheet" href="https://fonts.googleapis.com/css2?family=Poppins:wght@300;400;500&display=swap">
<style>
  :root {
    --page-bg: #2a2a2b;
    --card-top: #1c1d1f;
    --card-bottom: #2b2c2e;
    --teal: #5fa9a2;
    --purple: #7d4291;
    --text-light: #d9d9d9;
  }
  * { margin: 0; padding: 0; box-sizing: border-box; }
  html, body { width: 1200px; height: 1138px; overflow: hidden; }
  body {
    background: var(--page-bg);
    font-family: "Poppins", sans-serif;
    position: relative;
  }
  .card {
    position: absolute;
    width: 620px;
    height: 376px;
    border-radius: 16px;
    background: linear-gradient(160deg, var(--card-top) 0%, var(--card-bottom) 100%);
    overflow: hidden;
  }
  .card-front { left: 272px; top: 184px; }
  .card-back  { left: 274px; top: 606px; }

  .brand-name {
    position: absolute;
    color: var(--teal);
    font-weight: 400;
    white-space: nowrap;
    display: flex;
    align-items: center;
    gap: 12px;
  }
  .brand-dot {
    width: 12px; height: 12px;
    border-radius: 50%;
    background: var(--purple);
  }
  .card-front .brand-name {
    font-size: 54px;
    left: 0; right: 0;
    top: 142px;
    justify-content: center;
  }
  .card-back .brand-name {
    font-size: 38px;
    right: 40px;
    top: 88px;
  }

  .front-web {
    position: absolute;
    left: 0; right: 0;
    top: 319px;
    display: flex;
    align-items: center;
    justify-content: center;
    gap: 24px;
  }
  .front-web .rule {
    width: 50px; height: 2px;
    background: var(--teal);
  }
  .front-web .url {
    color: var(--purple);
    font-size: 15px;
    font-weight: 300;
    letter-spacing: 4.2px;
  }

  .person {
    position: absolute;
    left: 35px;
    top: 198px;
  }
  .person-name {
    color: var(--teal);
    font-size: 27px;
    font-weight: 400;
    line-height: 1.2;
  }
  .person-role {
    color: var(--text-light);
    font-size: 16px;
    font-weight: 300;
    margin-top: 2px;
  }

  .contact-list {
    position: absolute;
    left: 35px;
    top: 274px;
    list-style: none;
  }
  .contact-list li {
    display: flex;
    align-items: center;
    height: 27px;
    color: var(--text-light);
    font-size: 17px;
    font-weight: 300;
  }
  .contact-list svg {
    width: 16px; height: 16px;
    margin-right: 16px;
    flex: none;
  }

  .address {
    position: absolute;
    right: 34px;
    top: 297px;
    text-align: right;
    color: var(--text-light);
    font-size: 16px;
    font-weight: 300;
    line-height: 26px;
  }

  .accent-band {
    position: absolute;
    left: 0; right: 0; bottom: 0;
    height: 10px;
    display: flex;
  }
  .accent-band .teal { flex: 1; background: var(--teal); }
  .accent-band .purple { flex: 1; background: var(--purple); }
</style>
</head>
<body>

  <section class="card card-front">
    <div class="brand-name"><span class="brand-dot"></span>Velora Health</div>
    <div class="front-web">
      <span class="rule"></span>
      <span class="url">www.velorahealth.com</span>
      <span class="rule"></span>
    </div>
  </section>

  <section class="card card-back">
    <div class="brand-name"><span class="brand-dot"></span>Velora Health</div>

    <div class="person">
      <div class="person-name">Mara Velora</div>
      <div class="person-role">Health Advisor</div>
    </div>

    <ul class="contact-list">
      <li>
        <svg viewBox="0 0 16 16" aria-hidden="true">
          <path d="M2 6c0-2 2-3 6-3s6 1 6 3l-2 1-1-2H5L4 7z" fill="#7d4291"/>
          <rect x="4" y="8" width="8" height="6" rx="1" fill="#7d4291"/>
        </svg>00-000-0000
      </li>
      <li>
        <svg viewBox="0 0 16 16" aria-hidden="true">
          <rect x="1" y="3" width="14" height="10" fill="#5fa9a2"/>
          <path d="M1 3l7 6 7-6" fill="none" stroke="#1e1f21" stroke-width="1.3"/>
        </svg>mara@velorahealth.com
      </li>
      <li>
        <svg viewBox="0 0 16 16" aria-hidden="true">
          <circle cx="8" cy="8" r="6.5" fill="none" stroke="#7d4291" stroke-width="1.3"/>
          <ellipse cx="8" cy="8" rx="3" ry="6.5" fill="none" stroke="#7d4291" stroke-width="1.1"/>
          <path d="M1.5 8h13M2.5 5h11M2.5 11h11" stroke="#7d4291" stroke-width="1"/>
        </svg>www.velorahealth.com
      </li>
    </ul>

    <address class="address" style="font-style:normal">
      234 Anywhere St.,<br>Any City, US 123456
    </address>

    <div class="accent-band"><span class="teal"></span><span class="purple"></span></div>
  </section>

</body>
</html>
```